Local Roofing/Construction company business needs new biz card design

We need a new business card design, current cards are from the start of this operation and generic at best. We are a local Construction Company (General Contractor) with a majority of our work originating from insurance claims-exterior finish work is the main focus (Roofs-Siding-Gutters etc). Heavily involved with homeowners and the low ball offers they receive from insurance company's after a insurable event takes place. I have attached some of our original logo file(s) below.

```html
<!DOCTYPE html>
<html lang="en">
<head>
<meta charset="utf-8">
<title>Northgate Construction – Business Card</title>
<link rel="stylesheet" href="https://fonts.googleapis.com/css2?family=Lato:wght@400;700&family=Montserrat:wght@500;600;800&display=swap">
<style>
  :root {
    --brand-green: #22d877;
    --ink: #101a1d;
    --paper: #ffffff;
    --muted: #5b6366;
    --stage: #2b2e31;
  }
  * { box-sizing: border-box; margin: 0; padding: 0; }
  html, body {
    width: 1200px; height: 952px; overflow: hidden;
    background: var(--stage);
  }
  .sheet {
    width: 1200px; height: 952px;
    display: flex; flex-direction: column;
    align-items: center; justify-content: center; gap: 40px;
  }
  .card {
    width: 760px; height: 434px;
    border-radius: 22px;
    position: relative; overflow: hidden;
    box-shadow: 0 10px 30px rgba(0,0,0,.35);
  }

  /* Front */
  .card--front {
    background: var(--brand-green);
    display: flex; align-items: center; justify-content: center;
  }
  .brand {
    display: flex; align-items: center; gap: 18px;
    font-family: "Montserrat", sans-serif; font-weight: 800;
    color: var(--ink); text-transform: uppercase;
  }
  .brand__square { width: 46px; height: 46px; background: var(--ink); }
  .brand__name { font-size: 46px; letter-spacing: 2px; line-height: 1; }

  /* Back */
  .card--back { background: var(--paper); }
  .card--back .brand { position: absolute; left: 48px; top: 44px; gap: 12px; }
  .card--back .brand__square { width: 26px; height: 26px; background: var(--brand-green); }
  .card--back .brand__name { font-size: 24px; letter-spacing: 1px; }

  .contact {
    position: absolute; left: 48px; top: 150px;
    list-style: none;
    font-family: "Lato", sans-serif; font-size: 16px; color: var(--muted);
  }
  .contact__item { display: flex; align-items: flex-start; gap: 12px; margin-bottom: 12px; line-height: 1.3; }
  .contact__icon {
    flex: none; width: 22px; height: 22px; border-radius: 4px;
    background: var(--ink); display: flex; align-items: center; justify-content: center;
  }
  .contact__icon--accent { background: var(--brand-green); }
  .contact__icon svg { width: 14px; height: 14px; }

  .person {
    position: absolute; right: 70px; top: 190px; text-align: right;
    font-family: "Montserrat", sans-serif;
  }
  .person__name { font-size: 28px; font-weight: 500; color: var(--ink); letter-spacing: 1px; text-transform: uppercase; }
  .person__surname { color: var(--brand-green); font-weight: 800; }
  .person__role { font-family: "Lato", sans-serif; font-size: 19px; color: var(--muted); margin-top: 6px; }

  .accent-band {
    position: absolute; right: 0; top: 250px;
    width: 46px; height: 44px; background: var(--brand-green);
  }
</style>
</head>
<body>
<main class="sheet">

  <section class="card card--front" aria-label="Card front">
    <div class="brand">
      <span class="brand__square"></span>
      <span class="brand__name">Northgate Construction</span>
    </div>
  </section>

  <section class="card card--back" aria-label="Card back">
    <div class="brand">
      <span class="brand__square"></span>
      <span class="brand__name">Northgate Construction</span>
    </div>

    <ul class="contact">
      <li class="contact__item">
        <span class="contact__icon contact__icon--accent">
          <svg viewBox="0 0 14 14"><path d="M7 1a4 4 0 0 0-4 4c0 3 4 8 4 8s4-5 4-8a4 4 0 0 0-4-4z" fill="#fff"/><circle cx="7" cy="5" r="1.5" fill="#22d877"/></svg>
        </span>
        <span>1720 Alder Ridge Road<br>Springfield, IL 62704</span>
      </li>
      <li class="contact__item">
        <span class="contact__icon">
          <svg viewBox="0 0 14 14"><path d="M3 1.5l2.5 0 1 3-1.5 1a7 7 0 0 0 3.5 3.5l1-1.5 3 1v2.5c0 .6-.5 1-1 1A11 11 0 0 1 2 2.5c0-.5.4-1 1-1z" fill="#fff"/></svg>
        </span>
        <span>+00 987 654 32</span>
      </li>
      <li class="contact__item">
        <span class="contact__icon">
          <svg viewBox="0 0 14 14"><rect x="1.5" y="3" width="11" height="8" fill="none" stroke="#fff" stroke-width="1.3"/><path d="M1.5 3l5.5 4.5L12.5 3" fill="none" stroke="#fff" stroke-width="1.3"/></svg>
        </span>
        <span>hello@northgatebuild.com</span>
      </li>
      <li class="contact__item">
        <span class="contact__icon">
          <svg viewBox="0 0 14 14"><path d="M3 2l8 5-3.5.8L9.5 12l-1.5.7-2-4.2L3 11z" fill="#fff"/></svg>
        </span>
        <span>www.northgatebuild.com</span>
      </li>
    </ul>

    <div class="person">
      <p class="person__name">Daniel M. <span class="person__surname">Hartley</span></p>
      <p class="person__role">General Contractor</p>
    </div>

    <span class="accent-band"></span>
  </section>

</main>
</body>
</html>
```